Word Template for KOREL Polls

KOREL Polls stands for 'Kindred Outlook Readings Entered Locally Polls'. It is a collaborative research effort to format and combine multiple sources of public opinion data from around the world into merged datasets. We need a Microsoft Word template design for our research reports, dataset codebooks, crowdsourced development guidelines, and other documents that will be produced as part of the research and development. The template should match the website design and logo, which are attached to this contest (these are the files from previous successful design contests).

The main purpose will be to write reports discussing research and analysis. There will be lots data visualizations (bar charts, scatter plots, pie charts, histograms, trend line charts etc.) as well as tables, diargams, and photos mixed in wit all the text. A second purpose will be to write guidebooks to describe processes and teach others how to manage data, find variables, and write code, which will include screenshots and Word are diagrams and figures.

There are some document uploaded as examples for the kinds of things for which we need the template (working papers, codebooks, pamphlets, etc)

Target Market(s)

academia, government, non-profits, postgraduates, researchers

Font styles to use
Serif

Colors

Designer to choose colors to be used in the design.

Requirements
Must have
• A4 size page template
• Cover page
• Must match website design and logo (see attached)
Nice to have
• Colors to match logo and website (see attached)

```html
<!DOCTYPE html>
<html lang="en">
<head>
<meta charset="utf-8">
<title>KOREL Polls – Proposal Report Cover</title>
<link href="https://fonts.googleapis.com/css2?family=Carlito:wght@400;700&display=swap" rel="stylesheet">
<style>
  :root {
    --paper: #f9f9f9;
    --sky: #22a8e0;
    --navy: #2172b6;
    --white: #ffffff;
  }
  html, body {
    margin: 0;
    padding: 0;
    width: 927px;
    height: 1200px;
    overflow: hidden;
  }
  .cover {
    position: relative;
    width: 927px;
    height: 1200px;
    font-family: "Carlito", "Calibri", sans-serif;
    background: var(--sky);
  }
  .masthead {
    position: absolute;
    top: 0;
    left: 0;
    width: 100%;
    height: 376px;
    background: var(--paper);
  }
  .brand {
    position: absolute;
    right: 41px;
    top: 222px;
    display: flex;
    align-items: center;
    gap: 16px;
  }
  .brand-dot {
    width: 52px;
    height: 52px;
    border-radius: 50%;
    background: var(--sky);
  }
  .brand-name {
    font-size: 48px;
    font-weight: 700;
    color: var(--navy);
    line-height: 1;
    letter-spacing: 0.2px;
  }
  .doc-type {
    position: absolute;
    right: 42px;
    top: 296px;
    margin: 0;
    font-size: 39px;
    font-weight: 700;
    line-height: 1;
  }
  .doc-type .lead { color: var(--navy); }
  .doc-type .tail { color: var(--sky); }
  .title-block {
    position: absolute;
    right: 39px;
    top: 451px;
    text-align: right;
    color: var(--white);
  }
  .main-title {
    margin: 0;
    font-size: 38px;
    font-weight: 700;
    line-height: 1;
    letter-spacing: 0.3px;
  }
  .author {
    margin: 12px 0 0;
    font-size: 30px;
    font-weight: 400;
    line-height: 1;
  }
</style>
</head>
<body>
  <main class="cover">
    <header class="masthead">
      <div class="brand">
        <span class="brand-dot"></span>
        <span class="brand-name">KOREL Polls</span>
      </div>
      <p class="doc-type"><span class="lead">Proposal</span> <span class="tail">Report</span></p>
    </header>
    <section class="title-block">
      <h1 class="main-title">MAIN HEADING TITLE HERE</h1>
      <p class="author">Author/presented name</p>
    </section>
  </main>
</body>
</html>
```